Banner for a National Dental Conference

We need a banner logo for our next Dental Conference in 2017. Our theme is 'Challenging the Status Quo'.
It must have the words '20 years of oral health therapy in Victoria' and the conference date and venue:
7-8th April 2017
Bramwell The Orchards Resort, Torquay, Victoria.
It must also feature our association logo as attached.
Please be creative, however, we would like a 'clean' design, not cluttered.
The design is intended for use in the conference program and website.

Target Market(s)

Dental practitioners

Industry/Entity Type

Dental

Requirements
Must have
• As above.

```html
<!DOCTYPE html>
<html lang="en">
<head>
<meta charset="utf-8">
<title>Challenging the Status Quo – Conference Banners</title>
<link href="https://fonts.googleapis.com/css2?family=Orbitron:wght@500;700&family=Teko:wght@400;500;600&display=swap" rel="stylesheet">
<style>
  :root {
    --purple: #5a3a8e;
    --yellow: #f4ea1c;
    --white: #ffffff;
    --ink: #111111;
    --backdrop: #ecebe8;
    --photo-light: #f7f3f1;
    --photo-warm: #eadcd6;
  }
  * { box-sizing: border-box; margin: 0; padding: 0; }
  html, body { width: 1200px; height: 830px; overflow: hidden; }
  body { background: var(--backdrop); position: relative; font-family: "Teko", sans-serif; }

  .banner { position: absolute; background: var(--white); overflow: hidden; box-shadow: 0 2px 6px rgba(0,0,0,.25); }
  .banner--square { left: 412px; top: 34px; width: 538px; height: 449px; }
  .banner--leader { left: 26px; top: 592px; width: 1149px; height: 140px; }

  .photo { position: absolute; background: radial-gradient(ellipse at 55% 40%, var(--photo-warm), var(--photo-light) 70%, var(--white)); }
  .banner--square .photo { left: 0; top: 0; width: 400px; height: 449px; }
  .banner--leader .photo { left: 326px; top: 0; width: 290px; height: 140px; }

  .panel { position: absolute; inset: 0; width: 100%; height: 100%; }

  .theme { position: absolute; font-family: "Orbitron", sans-serif; color: var(--ink); line-height: 1; }
  .theme__lead { display: block; font-weight: 500; }
  .theme__main { display: block; font-weight: 700; }

  .assoc { position: absolute; font-family: "Teko", sans-serif; font-weight: 500; color: var(--purple); letter-spacing: 1px; line-height: 1; white-space: nowrap; }

  .anniv-number { position: absolute; font-family: "Teko", sans-serif; font-weight: 400; color: transparent; -webkit-text-stroke: 3px var(--white); line-height: .8; }
  .anniv-years { position: absolute; font-family: "Teko", sans-serif; font-weight: 600; color: var(--white); line-height: 1; }
  .anniv-sub { position: absolute; font-family: "Teko", sans-serif; font-weight: 500; color: var(--white); line-height: 1; text-transform: uppercase; }
  .event-date { position: absolute; font-family: "Teko", sans-serif; font-weight: 600; color: var(--yellow); line-height: 1; text-transform: uppercase; }
  .event-venue { position: absolute; font-family: "Teko", sans-serif; font-weight: 500; color: var(--white); line-height: 1.05; text-transform: uppercase; white-space: nowrap; }

  /* Square banner */
  .banner--square .theme { left: 20px; top: 24px; }
  .banner--square .theme__lead { font-size: 29px; }
  .banner--square .theme__main { font-size: 39px; margin-top: 2px; }
  .banner--square .anniv-number { right: 14px; top: 20px; font-size: 170px; }
  .banner--square .anniv-years { right: 18px; top: 128px; font-size: 62px; }
  .banner--square .anniv-sub { right: 18px; top: 192px; font-size: 27px; text-align: right; line-height: 1.12; }
  .banner--square .event-date { right: 18px; top: 358px; font-size: 30px; }
  .banner--square .event-venue { right: 18px; top: 390px; font-size: 25px; text-align: right; }
  .banner--square .assoc { left: 18px; top: 408px; font-size: 30px; }

  /* Leaderboard banner */
  .banner--leader .assoc { left: 100px; top: 10px; font-size: 30px; }
  .banner--leader .theme { left: 20px; top: 52px; }
  .banner--leader .theme__lead { font-size: 28px; }
  .banner--leader .theme__main { font-size: 38px; margin-top: 2px; }
  .banner--leader .anniv-number { left: 636px; top: 6px; font-size: 122px; }
  .banner--leader .anniv-years { left: 638px; top: 92px; font-size: 48px; }
  .banner--leader .anniv-sub { left: 769px; top: 8px; font-size: 30px; line-height: 1.14; }
  .banner--leader .event-date { left: 961px; width: 180px; text-align: center; top: 18px; font-size: 32px; }
  .banner--leader .event-venue { left: 951px; width: 200px; text-align: center; top: 56px; font-size: 21px; }
  .banner--leader .event-venue__name { display: block; font-size: 32px; font-weight: 600; line-height: 1; }
  sup { font-size: .55em; vertical-align: .7em; }
</style>
</head>
<body>

<section class="banner banner--square" aria-label="Conference banner, 300 by 250">
  <div class="photo" role="img" aria-label="Faded photograph of a smiling woman"></div>
  <svg class="panel" viewBox="0 0 538 449" preserveAspectRatio="none" aria-hidden="true">
    <polygon points="364,0 538,0 538,449 184,449" fill="var(--purple)"/>
  </svg>
  <h1 class="theme"><span class="theme__lead">Challenging the</span><span class="theme__main">Status Quo</span></h1>
  <div class="anniv-number">20</div>
  <div class="anniv-years">YEARS</div>
  <div class="anniv-sub">Of oral health<br>therapy in Victoria</div>
  <div class="event-date">7-8th April 2017</div>
  <div class="event-venue">Bramwell The Orchards Resort,<br>Torquay, Victoria</div>
  <div class="assoc">Coastline OHT</div>
</section>

<section class="banner banner--leader" aria-label="Conference banner, 486 by 60">
  <div class="photo" role="img" aria-label="Faded photograph of a smiling woman"></div>
  <svg class="panel" viewBox="0 0 1149 140" preserveAspectRatio="none" aria-hidden="true">
    <polygon points="640,0 1149,0 1149,140 582,140" fill="var(--purple)"/>
  </svg>
  <div class="assoc">Coastline OHT</div>
  <h2 class="theme"><span class="theme__lead">Challenging the</span><span class="theme__main">Status Quo</span></h2>
  <div class="anniv-number">20</div>
  <div class="anniv-years">YEARS</div>
  <div class="anniv-sub">Of oral<br>health<br>therapy in<br>Victoria</div>
  <div class="event-date">7-8<sup>th</sup> April 2017</div>
  <div class="event-venue"><span class="event-venue__name">Bramwell</span>The Orchards Resort<br>Torquay, Victoria</div>
</section>

</body>
</html>
```